Business Card design for new private practice opening

I need a business card design for my new private practice with my new logo uploaded as a file
On the front the logo
On the back: maybe a small logo somewhere?
Priv. Doz. DDr. Corinna Vestaluk
Fachärztin für Allgemein- & Viszeralchirurgie
Address: xxx
Tel: xxx
Mobil:xxx
Webseite:xxx
Email:xxx

Contact Information for Business Card

See project description above for details

Requirements
Nice to have
• I would like the colors of the logo incorporated into the business card

```html
<!DOCTYPE html>
<html lang="de">
<head>
<meta charset="utf-8">
<title>Vestaluk Chirurgie – Visitenkarte</title>
<link href="https://fonts.googleapis.com/css2?family=Montserrat:wght@500;600;700&display=swap" rel="stylesheet">
<style>
  :root {
    --teal: #48b8b6;
    --grey: #828282;
    --paper: #ffffff;
    --backdrop: #efefef;
  }
  * { box-sizing: border-box; margin: 0; padding: 0; }
  html, body { width: 1200px; height: 1000px; overflow: hidden; }
  body {
    background: var(--backdrop);
    font-family: "Montserrat", Arial, sans-serif;
    position: relative;
  }
  .card {
    position: absolute;
    left: 295px;
    width: 590px;
    height: 346px;
  }
  .card-front { top: 83px; background: var(--teal); }
  .card-back { top: 498px; background: var(--paper); }

  .front-mark {
    position: absolute;
    left: 50%; top: 50%;
    width: 330px; height: 330px;
    transform: translate(-50%, -50%);
  }
  .front-name {
    position: absolute;
    inset: 0;
    display: flex;
    flex-direction: column;
    align-items: center;
    justify-content: center;
    color: var(--paper);
    font-weight: 600;
    font-size: 28px;
    line-height: 1.15;
    letter-spacing: 0.5px;
  }

  .brand {
    position: absolute;
    left: 145px; top: 39px;
    display: flex;
    align-items: center;
    gap: 16px;
  }
  .brand-circle { width: 88px; height: 88px; flex: none; }
  .brand-name {
    color: var(--grey);
    font-weight: 600;
    font-size: 35px;
    line-height: 37px;
    letter-spacing: 0.3px;
  }

  .person {
    position: absolute;
    left: 68px; top: 156px;
  }
  .person-name {
    color: var(--teal);
    font-weight: 700;
    font-size: 16px;
    line-height: 20px;
  }
  .person-title {
    color: var(--grey);
    font-weight: 500;
    font-size: 16px;
    line-height: 20px;
  }
  .contact {
    list-style: none;
    margin-top: 12px;
    color: var(--teal);
    font-weight: 500;
    font-size: 16px;
    line-height: 20.5px;
  }
</style>
</head>
<body>
  <section class="card card-front">
    <svg class="front-mark" viewBox="0 0 330 330" aria-hidden="true">
      <circle cx="165" cy="165" r="159" fill="none" stroke="var(--paper)" stroke-width="12"/>
    </svg>
    <div class="front-name">
      <span>VESTALUK</span>
      <span>CHIRURGIE</span>
    </div>
  </section>

  <section class="card card-back">
    <div class="brand">
      <svg class="brand-circle" viewBox="0 0 88 88" aria-hidden="true">
        <circle cx="44" cy="44" r="42" fill="none" stroke="var(--grey)" stroke-width="3"/>
      </svg>
      <div class="brand-name">VESTALUK<br>CHIRURGIE</div>
    </div>

    <div class="person">
      <p class="person-name">Priv. Doz. DDr. CORINNA VESTALUK</p>
      <p class="person-title">Fachärztin für Allgemein- &amp; Viszeralchirurgie</p>
      <ul class="contact">
        <li>Address: xxx</li>
        <li>Tel: xxx</li>
        <li>Mobil:xxx</li>
        <li>Webseite:xxx</li>
        <li>Email:xxx</li>
      </ul>
    </div>
  </section>
</body>
</html>
```